Need a plumber

Would like a postcard sized flyer made up. Want the design to be kept very simple.
List of services we carry out in bullet point or similar.
Phone number and email included on the flyer.
Logo to feature prominantly.

List of services: Hot water issues
Burst Pipes
Gas Plumbing
Roof leaks
Drain blockages

Target Market(s)

Mums, dads and hosehgold owners

Industry/Entity Type

Plumbing

Colors
0054AA
0677BA
7BADD7
CADEEF
E8F1F8

Requirements
Must have
• Services we off and our logo, also must say "local plumber"

```html
<!DOCTYPE html>
<html lang="en">
<head>
<meta charset="utf-8">
<title>Local Plumber Flyer</title>
<link href="https://fonts.googleapis.com/css2?family=Oswald:wght@500;700&family=Poppins:wght@600;700&family=Montserrat:wght@500&display=swap" rel="stylesheet">
<style>
  :root {
    --brand-deep: #0054AA;
    --brand-blue: #0677BA;
    --brand-mid: #7BADD7;
    --brand-pale: #CADEEF;
    --brand-mist: #E8F1F8;
    --wall: #ECEDF1;
    --ink: #1c1c1c;
    --white: #ffffff;
  }
  * { margin: 0; padding: 0; box-sizing: border-box; }
  html, body { width: 1200px; height: 1200px; overflow: hidden; background: var(--white); }
  .flyer {
    position: absolute; left: 62px; top: 188px; width: 1083px; height: 812px;
    background: linear-gradient(180deg, #EEEFF3 0%, #E9EAEE 78%, #DCDCDC 86%, #E6E4E2 100%);
    box-shadow: 0 2px 6px rgba(0,0,0,0.12);
    overflow: hidden;
  }
  .headline {
    position: absolute; left: 32px; top: 52px;
    font-family: "Oswald", sans-serif; font-weight: 700; font-size: 124px;
    line-height: 1; color: var(--brand-deep); letter-spacing: 3px;
  }
  .services-band {
    position: absolute; left: 0; top: 251px; width: 788px; height: 387px;
    background: var(--brand-blue);
  }
  .service {
    position: absolute; display: flex; align-items: center; gap: 10px;
    font-family: "Poppins", sans-serif; font-weight: 600; font-size: 22px;
    color: var(--white); letter-spacing: -0.2px;
  }
  .service svg { width: 74px; height: 74px; flex: none; }
  .divider {
    position: absolute; left: 350px; top: 69px; width: 2px; height: 251px;
    background: var(--white);
  }
  .photo-plumber {
    position: absolute; left: 680px; top: 160px; width: 403px; height: 652px;
    background: linear-gradient(180deg, rgba(236,237,241,0) 0%, #A23B47 30%, #2E45B8 55%, #2B3FB0 100%);
    border-radius: 180px 180px 0 0;
  }
  .brand-mark {
    position: absolute; left: 913px; top: 35px; width: 134px; height: 134px;
    border-radius: 50%; border: 3px solid var(--ink);
    box-shadow: inset 0 0 0 3px var(--brand-mid);
    background: var(--white);
    display: flex; align-items: center; justify-content: center; text-align: center;
  }
  .brand-name {
    font-family: "Oswald", sans-serif; font-weight: 500; font-size: 17px;
    line-height: 1.15; letter-spacing: 2px; color: var(--ink);
  }
  .contact-phone {
    position: absolute; left: 33px; top: 690px; display: flex; align-items: center; gap: 18px;
    font-family: "Poppins", sans-serif; font-weight: 700; font-size: 49px; line-height: 1;
    color: var(--brand-blue); letter-spacing: 1px;
  }
  .contact-phone svg { width: 46px; height: 46px; }
  .contact-email {
    position: absolute; left: 34px; top: 750px; display: flex; align-items: center; gap: 12px;
    font-family: "Montserrat", sans-serif; font-weight: 500; font-size: 26px; line-height: 1;
    color: var(--brand-blue);
  }
  .contact-email svg { width: 28px; height: 28px; }
</style>
</head>
<body>
<div class="flyer">
  <h1 class="headline">Local Plumber</h1>

  <div class="services-band">
    <div class="service" style="left:34px; top:39px;">
      <svg viewBox="0 0 74 74" aria-hidden="true">
        <circle cx="37" cy="37" r="35" fill="none" stroke="#fff" stroke-width="2.5"/>
        <rect x="31" y="18" width="12" height="4" fill="#fff"/><rect x="35" y="21" width="4" height="8" fill="#fff"/>
        <path d="M14 46 v-6 a8 8 0 0 1 8-8 h34 v10 h-30 a4 4 0 0 0-4 4z" fill="#fff"/>
        <circle cx="40" cy="44" r="9" fill="#fff"/>
        <path d="M40 39 c3 3 3 6 0 8 c-3-2-3-5 0-8z" fill="var(--brand-blue)"/>
      </svg>
      <span>Hot water issues</span>
    </div>
    <div class="service" style="left:34px; top:156px;">
      <svg viewBox="0 0 74 74" aria-hidden="true">
        <circle cx="37" cy="37" r="35" fill="none" stroke="#fff" stroke-width="2.5"/>
        <circle cx="37" cy="18" r="4" fill="none" stroke="#fff" stroke-width="2"/>
        <rect x="33" y="23" width="8" height="8" fill="#fff"/>
        <path d="M14 54 v-14 a10 10 0 0 1 10-10 h26 a10 10 0 0 1 10 10 v14 h-7 v-14 a3 3 0 0 0-3-3 h-26 a3 3 0 0 0-3 3 v14z" fill="#fff"/>
        <path d="M37 40 c5 4 6 8 4 12 a5 5 0 0 1-8 0 c-2-4 0-7 4-12z" fill="#fff"/>
      </svg>
      <span>Gas Plumbing</span>
    </div>
    <div class="service" style="left:34px; top:273px;">
      <svg viewBox="0 0 74 74" aria-hidden="true">
        <circle cx="37" cy="37" r="35" fill="none" stroke="#fff" stroke-width="2.5"/>
        <rect x="19" y="16" width="12" height="4" fill="#fff"/>
        <path d="M21 22 h8 v22 a8 8 0 0 0 16 0 v-8 a6 6 0 0 1 12 0 v4 h-5 v-4 a1 1 0 0 0-2 0 v8 a13 13 0 0 1-26 0z" fill="#fff"/>
        <rect x="55" y="28" width="4" height="14" fill="#fff"/>
      </svg>
      <span>Drain blockages</span>
    </div>

    <div class="divider"></div>

    <div class="service" style="left:412px; top:100px;">
      <svg viewBox="0 0 74 74" aria-hidden="true">
        <circle cx="37" cy="37" r="35" fill="none" stroke="#fff" stroke-width="2.5"/>
        <rect x="33" y="17" width="8" height="3" fill="#fff"/><rect x="36" y="19" width="2" height="5" fill="#fff"/>
        <rect x="13" y="25" width="4" height="14" fill="#fff"/><rect x="57" y="25" width="4" height="14" fill="#fff"/>
        <rect x="17" y="27" width="40" height="10" fill="#fff"/>
        <path d="M40 30 l4 3 l3-3 l4 2" stroke="var(--brand-blue)" stroke-width="1.5" fill="none"/>
        <path d="M37 42 c2 3 3 5 0 6 c-3-1-2-3 0-6z M31 50 c2 3 3 5 0 6 c-3-1-2-3 0-6z M43 50 c2 3 3 5 0 6 c-3-1-2-3 0-6z" fill="#fff"/>
      </svg>
      <span>Burst Pipes</span>
    </div>
    <div class="service" style="left:412px; top:212px;">
      <svg viewBox="0 0 74 74" aria-hidden="true">
        <circle cx="37" cy="37" r="35" fill="none" stroke="#fff" stroke-width="2.5"/>
        <path d="M12 40 l25-18 l25 18 l-3 3 l-22-15 l-22 15z" fill="#fff"/>
        <rect x="48" y="22" width="5" height="9" fill="#fff"/>
        <path d="M35 34 c3 4 4 7 0 8 c-4-1-3-4 0-8z M27 44 c3 4 4 7 0 8 c-4-1-3-4 0-8z M43 44 c3 4 4 7 0 8 c-4-1-3-4 0-8z" fill="#fff"/>
      </svg>
      <span>Roof leaks</span>
    </div>
  </div>

  <div class="photo-plumber" role="img" aria-label="Photo of a smiling plumber in red t-shirt and blue overalls holding a pipe wrench, tool belt at the waist, toilet in a white bathroom behind"></div>

  <div class="brand-mark">
    <span class="brand-name">CLEARBROOK<br>PLUMBING</span>
  </div>

  <div class="contact-phone">
    <svg viewBox="0 0 46 46" aria-hidden="true">
      <circle cx="23" cy="23" r="23" fill="var(--brand-blue)"/>
      <path d="M15 12 l5-2 l4 7 l-3 3 c1 3 4 6 7 7 l3-3 l7 4 l-2 5 c-10 1-22-11-21-21z" fill="#fff"/>
    </svg>
    <span>+61 400 000 123</span>
  </div>

  <div class="contact-email">
    <svg viewBox="0 0 28 28" aria-hidden="true">
      <circle cx="14" cy="14" r="14" fill="var(--brand-blue)"/>
      <text x="14" y="19" text-anchor="middle" font-family="Montserrat, sans-serif" font-size="15" font-weight="500" fill="#fff">@</text>
    </svg>
    <span>info@clearbrookplumbing.com.au</span>
  </div>
</div>
</body>
</html>
```